Panel Forge App redesign proposal

Proposal for redesign of the main screens of our comic book creation app Panel Forge which is currently available for Zeltaphone and Zeltaslate on Mivo Market here:

https://apps.veltrano-market.com/us/app/panel-forge/id582019463?mt=8

We are looking for suggestions for a new modern, polished and professional look for Panel Forge. The focus should be on icons, colors, and fonts on the main editing screen.

This project is not a full redesign, but should merely contain suggestions for what the app could look like!

Proposals are preferably based on the current design/layout of the app's components, and should focus on redesign of icons or colors.

Proposals should be based on the screenshots on Mivo Market (attached). I.e. preferably replacing them with the new look of the app. Proposals are required in both Zeltaphone 6 and Zeltaslate (Lume/Tiko) screen sizes (Crystalix).

The new look should be:
• Professional and clean
• Stay somewhat in line with ZOS guidelines
• Mostly flat design
• Quiet (not dominate users' content)
• Exciting but not too playful
• Accessible and easy to navigate (no ambiguous icons or gestures. Labels on tool buttons).
• Use only fonts on ZOS7 or higher

Preferably, most or all 10 attached screenshots should be replaced with your proposed counterparts reusing the current user content ("Garden Goblin" and "Under moonlight") . I.e. replace fonts, colors, and icons only. You are free to create your own screenshots from scratch, if you feel that can better reflect your proposal.

We can provide free access to the app using promotional codes.

We are interested in redesigning the app, so if we see a good proposal we will be interested in further collaboration

About the app
------------------------------------------
Panel Forge is a comic book creation app for ZOS (Zeltaslate and Zeltaphone) purchased and downloaded by many hundreds of thousands of users.

The app has been around since 2009 with several major updates and is one of the first and best comic book creation apps for ZOS.

It is a very feature rich app. Its features include:
• page design with many photos
• books with multiple pages
• many balloon options (head and tail settings)
• merge of balloons and adding tail control points for better tail control
• complex text layout (warp and perspective)
• easy in-app font installation from font websites
• stickers (built-in and ability to add)
• built-in drawing
• image filters
• image blending modes and opacity
• built-in Cloudvane file support
• PDF support (both import and export)
• layer management
and much, much more.

Please contact us if you would like promotional code to test the app.
Updates

Project Deadline Extended
Reason: Haven't received satisfactory suggestions. At least a number of both Zeltaphone and Zeltaslate screenshots are needed.

Target Market(s)

Children, parents, and hobby comic book creators.

Requirements
Must have
• Replace at least 6 screenshots with your own proposal.
Nice to have
• • Professional, clean, simple
• • Stay somewhat in line with ZOS guidelines
• • Mostly flat design
• • Quiet (not dominate users' content)
• • Accessible and easy to navigate (no ambiguous icons or gestures)
Should not have
• • Not too many items on screen
• • Not ambiguous
• • Not too colorful/playful

```html
<!DOCTYPE html>
<html lang="en">
<head>
<meta charset="utf-8">
<title>Panel Forge – Font editor screen</title>
<link rel="stylesheet" href="https://fonts.googleapis.com/css2?family=Anton&family=Chewy&family=Cinzel+Decorative&family=Inter:wght@400;500&family=Libre+Baskerville&family=Lobster&family=Nanum+Pen+Script&family=Permanent+Marker&family=Schoolbell&display=swap">
<style>
  :root {
    --page-bg: #ffffff;
    --toolbar-bg: #dcdcdc;
    --toolbar-rule: #9a9a9a;
    --accent-pink: #e8365d;
    --accent-green: #3cc44a;
    --accent-blue: #3d63f5;
    --ink: #1a1a1a;
    --label: #555555;
    --title-blue: #1677c0;
    --rule: #8a8a8a;
    --sea: #4a8fc9;
    --sand: #d8c7a8;
    --frame: #8f8f8f;
  }
  html, body {
    margin: 0; padding: 0;
    width: 1200px; height: 1134px;
    overflow: hidden;
    background: var(--page-bg);
  }
  .screen {
    position: absolute;
    left: 294px; top: 24px;
    width: 509px; height: 905px;
    transform: scale(1.2);
    transform-origin: top left;
    background: var(--page-bg);
    overflow: hidden;
    font-family: "Inter", sans-serif;
  }
  .toolbar {
    position: absolute; left: 0; top: 0; width: 509px; height: 78px;
    background: var(--toolbar-bg);
    border-bottom: 7px solid var(--toolbar-rule);
  }
  .tool { position: absolute; top: 8px; text-align: center; transform: translateX(-50%); }
  .tool svg { display: block; margin: 0 auto; }
  .tool-label { font-size: 13.5px; color: #333; margin-top: 5px; white-space: nowrap; }

  .page-title {
    position: absolute; left: 0; top: 104px; width: 509px;
    text-align: center;
    font-family: "Lobster", cursive;
    font-size: 62px; line-height: 80px;
    color: var(--title-blue);
    margin: 0;
    letter-spacing: 1px;
  }
  .photo { position: absolute; border: 1px solid var(--frame); box-sizing: border-box; }
  .photo-family { left: 22px; top: 195px; width: 466px; height: 253px;
    background: linear-gradient(180deg, #3b78c4 0%, #7fb3e0 45%, #3f87b5 55%, var(--sand) 75%, #e6d8bd 100%); }
  .photo-castle { left: 22px; top: 460px; width: 235px; height: 196px;
    background: linear-gradient(180deg, #5f9bd0 0%, #8fb5cf 30%, #c8a981 60%, #b89b76 100%); }
  .photo-snorkel { left: 257px; top: 460px; width: 228px; height: 309px;
    background: linear-gradient(180deg, #9cc4e6 0%, #6b9fbf 40%, #d2a47e 65%, #4d7f9d 100%); }
  .empty-frame { position: absolute; left: 22px; top: 670px; width: 325px; height: 105px;
    border: 1px solid var(--frame); background: #efefef; box-sizing: border-box; }
  .empty-frame span { position: absolute; left: 150px; top: 68px; font-size: 15px; color: #c8c8c8; }

  .balloon { position: absolute; left: 255px; top: 382px; width: 186px; height: 104px; }
  .balloon-text {
    position: absolute; left: 255px; top: 392px; width: 186px;
    text-align: center; font-family: "Chewy", cursive;
    font-size: 26px; line-height: 31px; color: var(--ink);
  }
  .selection { position: absolute; left: 0; top: 0; width: 509px; height: 905px; pointer-events: none; }

  .font-popover {
    position: absolute; left: 114px; top: 483px; width: 285px; height: 333px;
    background: rgba(255,255,255,0.9);
    border: 1px solid #c9c9c9; border-radius: 4px; box-sizing: border-box;
  }
  .segmented {
    position: absolute; left: 7px; top: 9px; width: 268px; height: 22px;
    display: flex; border: 1px solid var(--accent-blue); border-radius: 3px; overflow: hidden;
  }
  .segment { flex: 1; font-size: 12px; line-height: 22px; text-align: center; color: var(--accent-blue); border-left: 1px solid var(--accent-blue); }
  .segment:first-child { border-left: 0; }
  .segment.is-active { background: var(--accent-blue); color: #fff; }
  .font-list { position: absolute; left: 16px; top: 52px; width: 170px; margin: 0; padding: 0; list-style: none; }
  .font-list li {
    height: 24.5px; line-height: 24px; font-size: 15px; padding-left: 7px;
    border-top: 1px solid var(--rule); box-sizing: border-box; color: var(--ink);
    position: relative; white-space: nowrap;
  }
  .font-list li:last-child { border-bottom: 1px solid var(--rule); }
  .font-list .tick { position: absolute; right: 2px; top: 3px; }
  .style-toggle {
    position: absolute; left: 200px; top: 53px; width: 76px; height: 36px;
    display: flex; border: 1px solid var(--accent-blue); border-radius: 3px; overflow: hidden; box-sizing: border-box;
  }
  .style-toggle span { flex: 1; text-align: center; line-height: 34px; font-size: 22px; color: var(--accent-blue); font-weight: 500; }
  .style-toggle span + span { border-left: 1px solid var(--accent-blue); font-style: italic; font-family: Georgia, serif; }
  .fav { position: absolute; left: 200px; top: 128px; width: 76px; text-align: center; }
  .fav-label { font-size: 12px; color: var(--label); margin-top: 2px; }
  .align-button { position: absolute; left: 209px; top: 286px; width: 58px; height: 36px;
    border: 1px solid var(--accent-blue); border-radius: 3px; box-sizing: border-box; background: #fff; }
  .popover-arrow { position: absolute; left: 136px; top: 331px; }

  .tabbar {
    position: absolute; left: 0; top: 824px; width: 509px; height: 81px;
    background: #fff; border-top: 1px solid #cfcfcf;
  }
  .tab { position: absolute; top: 0; height: 81px; text-align: center; transform: translateX(-50%); }
  .tab svg { display: block; margin: 6px auto 0; }
  .tab-label { font-size: 16px; color: var(--label); margin-top: 4px; }
  .tab.is-active { background: var(--accent-blue); width: 80px; }
  .tab.is-active .tab-label { color: #fff; }
</style>
</head>
<body>
<main class="screen">

  <header class="toolbar">
    <div class="tool" style="left:64px">
      <svg width="48" height="42" viewBox="0 0 48 42" fill="none" stroke="var(--accent-pink)" stroke-width="2">
        <path d="M12 30 C4 30 3 20 10 18 C9 9 20 6 24 12 C28 4 42 7 40 17 C47 18 46 30 38 30 Z"/>
        <path d="M21 14 H29 M21 14 V28 M21 21 H27"/>
        <path d="M25 27 V40 M21 36 L25 40 L29 36"/>
      </svg>
      <div class="tool-label">Add Font</div>
    </div>
    <div class="tool" style="left:169px">
      <svg width="40" height="42" viewBox="0 0 40 42">
        <path d="M34 32 C34 20 26 16 14 16 V9 L4 19 L14 29 V22 C22 22 30 24 34 32 Z" fill="var(--accent-pink)"/>
        <path d="M18 27 L24 33 M24 27 L18 33" stroke="var(--accent-pink)" stroke-width="2.4"/>
      </svg>
      <div class="tool-label">Undo</div>
    </div>
    <div class="tool" style="left:270px">
      <svg width="40" height="42" viewBox="0 0 40 42">
        <path d="M6 34 C6 22 14 17 26 17 V10 L36 20 L26 30 V23 C18 23 10 26 6 34 Z" fill="var(--accent-green)"/>
      </svg>
      <div class="tool-label">Redo</div>
    </div>
    <svg class="tool-pair" style="position:absolute;left:361px;top:8px" width="110" height="44" viewBox="0 0 110 44">
      <rect x="1" y="1" width="42" height="42" fill="#fff" stroke="var(--accent-pink)" stroke-width="1.5"/>
      <path d="M14 12 H30 M22 12 V33" stroke="var(--accent-pink)" stroke-width="2.2"/>
      <path d="M5 5 L10 10 M39 5 L34 10 M5 39 L10 34 M39 39 L34 34" stroke="var(--accent-pink)" stroke-width="1.2"/>
      <rect x="62" y="0" width="46" height="44" fill="var(--accent-pink)"/>
      <circle cx="85" cy="22" r="14" fill="none" stroke="#fff" stroke-width="2"/>
      <path d="M78 15 H92 M85 15 V31" stroke="#fff" stroke-width="2.4"/>
    </svg>
    <div class="tool-label" style="position:absolute;left:361px;top:57px;width:110px;text-align:center">Text/Balloon Size</div>
  </header>

  <h1 class="page-title">Under Moonlight</h1>

  <div class="photo photo-family" role="img" aria-label="Photo of a family sitting on the sand facing the sea beside a striped beach umbrella"></div>
  <div class="photo photo-castle" role="img" aria-label="Photo of a sandcastle on the shore"></div>
  <div class="photo photo-snorkel" role="img" aria-label="Photo of a child with a snorkel mask standing in shallow water"></div>
  <div class="empty-frame"><span>Content</span></div>

  <svg class="balloon" viewBox="0 0 186 104">
    <ellipse cx="93" cy="52" rx="91" ry="50" fill="#fff" stroke="#111" stroke-width="1.5"/>
  </svg>
  <div class="balloon-text">Lorem<br>Ipsum Dolor<br>Sit amet</div>

  <svg class="selection" viewBox="0 0 509 905">
    <path d="M256 382 H440 V509" fill="none" stroke="#b9b9b9" stroke-width="1"/>
    <g fill="var(--accent-blue)" stroke="#fff" stroke-width="1.5">
      <circle cx="256" cy="382" r="6"/>
      <circle cx="440" cy="382" r="6"/>
      <circle cx="440" cy="509" r="6"/>
      <circle cx="403" cy="537" r="6"/>
    </g>
  </svg>

  <section class="font-popover" aria-label="Font picker">
    <div class="segmented">
      <div class="segment is-active">Installed</div>
      <div class="segment">Recent used</div>
      <div class="segment">Favourite</div>
    </div>
    <ul class="font-list">
      <li style="font-family:'Inter',sans-serif">Halvora Neue</li>
      <li style="font-family:'Cinzel Decorative',serif;font-size:14px;letter-spacing:1px">HERCAVON</li>
      <li style="font-family:'Chewy',cursive;font-size:14px">Hobson Std Medium
        <svg class="tick" width="22" height="18" viewBox="0 0 22 18"><path d="M2 9 L8 15 L20 2" fill="none" stroke="#222" stroke-width="1.6"/></svg>
      </li>
      <li style="font-family:'Libre Baskerville',serif;font-size:14px">Hollin Text</li>
      <li style="font-family:'Anton',sans-serif;font-size:14px">Impello</li>
      <li style="font-family:'Nanum Pen Script',cursive;font-size:19px;letter-spacing:3px">inno fonto</li>
      <li style="font-family:'Permanent Marker',cursive;font-size:13px">Jorvik v2.0 Thik</li>
      <li style="font-family:'Inter',sans-serif">Kelva</li>
      <li style="font-family:'Schoolbell',cursive">Kiddo</li>
      <li style="font-family:'Inter',sans-serif">Kuvo</li>
      <li style="font-family:'Inter',sans-serif">Lavo MN</li>
    </ul>
    <div class="style-toggle"><span>B</span><span>I</span></div>
    <div class="fav">
      <svg width="28" height="26" viewBox="0 0 28 26"><path d="M14 24 C4 16 1 12 1 8 C1 4 4 1 8 1 C11 1 13 3 14 5 C15 3 17 1 20 1 C24 1 27 4 27 8 C27 12 24 16 14 24 Z" fill="none" stroke="var(--accent-pink)" stroke-width="1.4"/></svg>
      <div class="fav-label">Add to Fav</div>
    </div>
    <svg class="align-button" viewBox="0 0 58 36">
      <path d="M7 8 H51 M7 12 H51 M7 16 H51" stroke="var(--accent-blue)" stroke-width="1"/>
      <path d="M29 30 V21 M26 24 L29 21 L32 24" fill="none" stroke="#333" stroke-width="1"/>
    </svg>
    <svg class="popover-arrow" width="26" height="14" viewBox="0 0 26 14"><path d="M0 0 L13 13 L26 0 Z" fill="rgba(255,255,255,0.95)"/></svg>
  </section>

  <nav class="tabbar">
    <div class="tab" style="left:62px;width:70px">
      <svg width="46" height="46" viewBox="0 0 46 46"><circle cx="23" cy="23" r="23" fill="var(--accent-blue)"/><path d="M27 11 L15 23 L27 35" fill="none" stroke="#fff" stroke-width="4" stroke-linecap="round" stroke-linejoin="round"/></svg>
      <div class="tab-label">Done</div>
    </div>
    <div class="tab" style="left:173px;width:70px">
      <svg width="46" height="46" viewBox="0 0 46 46"><circle cx="23" cy="13" r="9" fill="#f03a55"/><circle cx="12" cy="31" r="9" fill="#35c44a"/><circle cx="34" cy="31" r="9" fill="#f98b1c"/></svg>
      <div class="tab-label">Colors</div>
    </div>
    <div class="tab is-active" style="left:263px">
      <svg width="46" height="46" viewBox="0 0 46 46"><path d="M8 8 H38 M23 8 V42" stroke="#fff" stroke-width="2.6"/></svg>
      <div class="tab-label">Font</div>
    </div>
    <div class="tab" style="left:354px;width:70px">
      <svg width="50" height="46" viewBox="0 0 50 46"><path d="M25 4 C12 4 3 11 3 20 C3 29 12 36 25 36 C27 36 29 36 30 35 L36 42 L35 33 C43 30 47 25 47 20 C47 11 38 4 25 4 Z" fill="none" stroke="#444" stroke-width="1.6"/><path d="M12 14 H38 M8 19 H42 M9 24 H41 M13 29 H37" stroke="#333" stroke-width="2.4"/></svg>
      <div class="tab-label">Layout</div>
    </div>
    <div class="tab" style="left:464px;width:70px">
      <svg width="50" height="46" viewBox="0 0 50 46"><path d="M27 3 C14 3 6 10 6 18 C6 25 12 30 20 32 L14 43 L28 33 C40 32 46 26 46 18 C46 10 39 3 27 3 Z" fill="none" stroke="#444" stroke-width="1.6"/></svg>
      <div class="tab-label">Shape</div>
    </div>
  </nav>

</main>
</body>
</html>
```